Stationery for a Messianic Congregation
Business Envelopes, Cards, Letterhead
Professional
Gregory T. Morrow
Ro'i
5142 Callaway Lane Orlando, FL 32867
gmorrow@ohelnoam.com
www.ohelnoam.com
Worship - Study - Fellowship

```html
<!DOCTYPE html>
<html lang="en">
<head>
<meta charset="utf-8">
<title>CedarHall Stationery</title>
<link href="https://fonts.googleapis.com/css2?family=Montserrat:wght@400;600;700&display=swap" rel="stylesheet">
<style>
:root{
  --bg:#ababab;
  --yellow:#f6cf16;
  --black:#1b1b1b;
  --white:#ffffff;
  --ink:#333333;
  --soft:#9a9a9a;
  --rule:#d6d6d6;
}
*{box-sizing:border-box;margin:0;padding:0}
html,body{width:1200px;height:269px;overflow:hidden}
body{background:var(--bg);font-family:"Montserrat",sans-serif;position:relative;color:var(--ink)}
.piece{position:absolute;box-shadow:1px 2px 4px rgba(0,0,0,.25);overflow:hidden}
.name{font-weight:600;color:var(--ink);white-space:nowrap;line-height:1}
.tiny{font-size:3px;line-height:4.5px;white-space:nowrap}
svg{position:absolute;left:0;top:0;width:100%;height:100%}

/* business cards */
.card-front{left:12px;top:55px;width:132px;height:70px;background:var(--black)}
.card-front .panel{position:absolute;left:0;top:0;width:58px;height:100%;background:var(--yellow);display:flex;align-items:center;justify-content:center}
.card-front .panel .name{font-size:7px;color:var(--black)}
.card-front .details{position:absolute;left:64px;top:18px;color:var(--white)}
.card-front .details .who{font-size:5px;font-weight:600;margin-bottom:3px}
.card-back{left:12px;top:132px;width:132px;height:72px;background:var(--black)}

/* letterhead */
.letterhead{left:152px;top:50px;width:112px;height:158px;background:var(--white)}
.letterhead .name{position:absolute;left:8px;top:11px;font-size:6px}
.letterhead .body{position:absolute;left:10px;top:40px;color:var(--soft)}
.letterhead .foot{position:absolute;left:8px;bottom:6px;color:var(--black);font-size:3px}

/* small cards */
.mini{width:48px;height:30px;background:var(--white)}
.mini .name{position:absolute;left:6px;top:12px;font-size:4.5px}
.mini-1{left:292px;top:96px}
.mini-2{left:292px;top:132px}
.mini-3{left:290px;top:190px;width:62px;height:32px}

/* envelopes */
.envelope{width:132px;height:46px;background:var(--white)}
.env-back{left:356px;top:168px}
.env-front{left:362px;top:188px}
.envelope .name{position:absolute;left:6px;top:7px;font-size:4.5px}

/* folder */
.folder{left:478px;top:22px;width:254px;height:232px;background:var(--white)}
.folder .cover-name{position:absolute;left:127px;width:127px;text-align:center;top:70px;font-size:7px}
.folder .tagline{position:absolute;left:127px;width:127px;text-align:center;top:86px;font-size:3.5px;color:var(--soft);white-space:nowrap}
.folder .pocket-card{position:absolute;left:80px;top:172px;width:52px;height:30px;background:var(--white);box-shadow:0 1px 3px rgba(0,0,0,.25)}
.folder .pocket-card .name{position:absolute;left:5px;top:12px;font-size:4px}

/* cd */
.cd-sleeve{left:744px;top:64px;width:108px;height:108px;background:var(--white)}
.cd{left:752px;top:74px;width:90px;height:90px;border-radius:50%;box-shadow:1px 2px 4px rgba(0,0,0,.3)}

/* fax */
.sheet-back{left:842px;top:160px;width:58px;height:92px;background:var(--white)}
.fax{left:900px;top:34px;width:158px;height:212px;background:var(--white)}
.fax .name{position:absolute;left:12px;top:13px;font-size:7px}
.fax h2{position:absolute;left:12px;top:40px;font-size:13px;font-weight:400;color:var(--ink)}
.fax .fields{position:absolute;left:12px;top:62px;width:134px}
.fax .row{display:flex;justify-content:space-between;border-bottom:.6px solid var(--rule);font-size:3.5px;padding:2px 0}
</style>
</head>
<body>

<div class="piece card-front">
  <div class="panel"><span class="name">CedarHall</span></div>
  <div class="details">
    <div class="who">Martin L. Hale</div>
    <div class="tiny">Ro'i</div>
    <div class="tiny">2290 Birchwood Drive Orlando, FL 32819</div>
    <div class="tiny">mhale@cedarhall.org</div>
    <div class="tiny">www.cedarhall.org</div>
  </div>
</div>

<div class="piece card-back">
  <svg viewBox="0 0 132 72">
    <path d="M14 14 H40 M14 14 V40" stroke="var(--yellow)" stroke-width="4" fill="none"/>
    <path d="M118 58 H92 M118 58 V32" stroke="var(--yellow)" stroke-width="4" fill="none"/>
    <rect x="40" y="30" width="52" height="12" fill="var(--yellow)"/>
  </svg>
</div>

<div class="piece letterhead">
  <svg viewBox="0 0 112 158"><path d="M0 140 Q60 118 112 128 V158 H0Z" fill="var(--yellow)"/></svg>
  <div class="name">CedarHall</div>
  <div class="body">
    <div class="tiny">Dear friends of the congregation,</div>
    <div class="tiny">we welcome you to join us for</div>
    <div class="tiny">worship, study and fellowship.</div>
  </div>
  <div class="foot">www.cedarhall.org</div>
</div>

<div class="piece mini mini-1"><div class="name">CedarHall</div></div>
<div class="piece mini mini-2"><svg viewBox="0 0 48 30"><path d="M0 22 Q24 14 48 20 V30 H0Z" fill="var(--yellow)"/></svg></div>
<div class="piece mini mini-3"><svg viewBox="0 0 62 32"><path d="M30 0 H62 V32 H20 Q40 16 30 0Z" fill="var(--yellow)"/></svg><div class="name">CedarHall</div></div>

<div class="piece envelope env-back"><svg viewBox="0 0 132 46"><path d="M0 0 L66 22 L132 0" stroke="var(--rule)" fill="none"/></svg></div>
<div class="piece envelope env-front">
  <svg viewBox="0 0 132 46"><path d="M0 38 Q70 30 132 34 V46 H0Z" fill="var(--yellow)"/></svg>
  <div class="name">CedarHall</div>
</div>

<div class="piece folder">
  <svg viewBox="0 0 254 232">
    <line x1="127" y1="0" x2="127" y2="232" stroke="var(--rule)" stroke-width="1"/>
    <path d="M0 160 H127" stroke="var(--rule)"/>
    <path d="M127 170 Q200 150 254 110 V232 H127Z" fill="var(--yellow)"/>
  </svg>
  <div class="name cover-name">CedarHall</div>
  <div class="tagline">Worship - Study - Fellowship</div>
  <div class="pocket-card"><div class="name">CedarHall</div></div>
</div>

<div class="piece cd-sleeve"><svg viewBox="0 0 108 108"><path d="M0 86 Q54 70 108 80 V108 H0Z" fill="var(--yellow)"/></svg></div>
<div class="piece cd">
  <svg viewBox="0 0 90 90">
    <circle cx="45" cy="45" r="45" fill="var(--white)"/>
    <path d="M45 0 A45 45 0 0 1 90 45 Q60 40 45 0Z" fill="var(--yellow)"/>
    <path d="M0 45 A45 45 0 0 0 45 90 Q40 60 0 45Z" fill="var(--yellow)"/>
    <circle cx="45" cy="45" r="8" fill="var(--bg)"/>
  </svg>
</div>

<div class="piece sheet-back"><svg viewBox="0 0 58 92"><path d="M0 70 Q30 58 58 62 V92 H0Z" fill="var(--yellow)"/></svg></div>
<div class="piece fax">
  <svg viewBox="0 0 158 212"><path d="M0 196 Q80 182 158 188 V212 H0Z" fill="var(--yellow)"/></svg>
  <div class="name">CedarHall</div>
  <h2>Fax</h2>
  <div class="fields">
    <div class="row"><span>To:</span><span>From: Martin L. Hale</span></div>
    <div class="row"><span>Fax:</span><span>Pages:</span></div>
    <div class="row"><span>Phone:</span><span>Date:</span></div>
    <div class="row"><span>Re:</span><span>CC:</span></div>
  </div>
</div>

</body>
</html>
```